" Iniciamos o projeto do cliente com análise do consumo de energia elétrica, a partir disso dimensionamos o sistema utilizando a melhor solução de energia solar fotovoltaica para o cliente. Elaboramos a proposta do projeto com o orçamento e após aceite do cliente iniciamos o processo de homologação junto às concessionárias e instalação do sistema no cliente com a nossa própria equipe técnica. Também apresentamos o saving e payback do projeto. "

```html
<!DOCTYPE html>
<html lang="pt-BR">
<head>
<meta charset="UTF-8">
<title>Radiar Energia Solar</title>
<link rel="stylesheet" href="https://fonts.googleapis.com/css2?family=Roboto:wght@400;700;900&family=Roboto+Condensed:wght@700&display=swap">
<style>
  :root{
    --navy:#1c2f5c;
    --navy-dark:#14234a;
    --orange:#f07c1e;
    --grey-text:#555b66;
    --page:#eef0f3;
    --white:#ffffff;
    --sky:#3d8fd6;
    --panel:#22366e;
  }
  *{margin:0;padding:0;box-sizing:border-box;}
  html,body{width:1200px;height:1200px;overflow:hidden;}
  body{background:var(--page);font-family:"Roboto",Arial,sans-serif;position:relative;}
  .banner{position:absolute;left:0;top:260px;width:1200px;height:680px;background:var(--white);overflow:hidden;}
  .hero-photo{position:absolute;left:0;top:0;}
  .brand{position:absolute;left:60px;top:60px;display:flex;align-items:center;gap:18px;}
  .brand-mark{width:74px;height:74px;border-radius:50%;background:var(--navy);}
  .brand-text{display:flex;flex-direction:column;}
  .brand-name{font-weight:700;font-size:66px;line-height:1;color:var(--navy);letter-spacing:1px;}
  .brand-tagline{font-weight:400;font-size:27px;letter-spacing:8px;color:var(--orange);margin-top:6px;}
  .section-title{position:absolute;left:34px;top:232px;display:flex;align-items:center;width:760px;}
  .section-title .marker{width:26px;height:20px;background:var(--orange);margin-right:14px;}
  .section-title h1{font-family:"Roboto Condensed",Arial,sans-serif;font-size:40px;color:var(--navy);white-space:nowrap;}
  .section-title .rule{flex:1;height:4px;background:var(--orange);margin-left:10px;margin-top:12px;}
  .feature{position:absolute;text-align:center;transform:translateX(-50%);}
  .feature svg{display:block;margin:0 auto 6px;}
  .feature h2{font-family:"Roboto Condensed",Arial,sans-serif;font-size:21px;color:var(--orange);letter-spacing:.5px;}
  .feature p{font-size:13.5px;line-height:1.3;color:var(--grey-text);margin-top:6px;}
  .photo-grid{position:absolute;left:798px;top:266px;width:402px;height:334px;display:grid;grid-template-columns:1fr 1fr;grid-template-rows:repeat(3,1fr);gap:4px;}
  .photo-grid div{background:linear-gradient(135deg,#5d8a5a,#2f4f86 60%,#b9c2cc);}
  .photo-grid div:nth-child(2n){background:linear-gradient(135deg,#c7cdd4,#24407c 55%,#6f9a63);}
  .photo-grid div:nth-child(5){background:linear-gradient(135deg,#c05a3a,#2a3f78 60%,#a9b3bd);}
  .footer-rule{position:absolute;left:0;top:628px;width:1200px;height:4px;background:var(--orange);}
  .footer-band{position:absolute;left:0;top:634px;width:1200px;height:46px;background:var(--navy-dark);}
</style>
</head>
<body>
  <section class="banner">
    <svg class="hero-photo" width="1200" height="210" viewBox="0 0 1200 210">
      <defs>
        <linearGradient id="heroFill" x1="0" y1="0" x2="0" y2="1">
          <stop offset="0" stop-color="var(--sky)"/>
          <stop offset="0.45" stop-color="#2c5ea8"/>
          <stop offset="1" stop-color="var(--panel)"/>
        </linearGradient>
      </defs>
      <polygon points="610,0 1200,0 1200,204 520,204" fill="var(--orange)"/>
      <polygon role="img" aria-label="Foto de painéis solares sobre telhado sob céu azul" points="624,0 1200,0 1200,204 536,204" fill="url(#heroFill)"/>
    </svg>

    <div class="brand">
      <div class="brand-mark"></div>
      <div class="brand-text">
        <span class="brand-name">Radiar</span>
        <span class="brand-tagline">ENERGIA SOLAR</span>
      </div>
    </div>

    <div class="section-title">
      <span class="marker"></span>
      <h1>Invista em energia solar</h1>
      <span class="rule"></span>
    </div>

    <div class="feature" style="left:161px;top:306px;width:180px;">
      <svg width="36" height="36" viewBox="0 0 36 36"><path d="M4 17 18 4l14 13" fill="none" stroke="var(--navy)" stroke-width="3"/><rect x="8" y="16" width="20" height="17" fill="none" stroke="var(--navy)" stroke-width="3"/><text x="18" y="30" text-anchor="middle" font-size="13" font-weight="700" fill="var(--navy)" font-family="Roboto,sans-serif">$</text></svg>
      <h2>ECONOMIA</h2>
      <p>Economize em até 95% seus gastos com a conta de luz.</p>
    </div>

    <div class="feature" style="left:396px;top:306px;width:230px;">
      <svg width="36" height="36" viewBox="0 0 36 36"><circle cx="18" cy="18" r="14" fill="none" stroke="var(--navy)" stroke-width="3"/><path d="M11 20c4-8 10-9 14-9-1 6-5 12-14 9z" fill="var(--navy)"/></svg>
      <h2>MEIO AMBIENTE</h2>
      <p>Comprometimento sustentável, com fonte de energia limpa, renovável e inesgotável.</p>
    </div>

    <div class="feature" style="left:628px;top:306px;width:180px;">
      <svg width="36" height="36" viewBox="0 0 36 36"><circle cx="18" cy="20" r="13" fill="none" stroke="var(--navy)" stroke-width="3"/><path d="M18 12v8l5 4" fill="none" stroke="var(--navy)" stroke-width="3"/><rect x="14" y="2" width="8" height="4" fill="var(--navy)"/></svg>
      <h2>LONGEVIDADE</h2>
      <p>Vida útil de, no mínimo, 25 anos.</p>
    </div>

    <div class="feature" style="left:170px;top:454px;width:150px;">
      <svg width="36" height="36" viewBox="0 0 36 36"><path d="M6 30 24 12M22 6a7 7 0 0 0 8 8" fill="none" stroke="var(--navy)" stroke-width="4" stroke-linecap="round"/><path d="M8 6l22 24" stroke="var(--navy)" stroke-width="4" stroke-linecap="round"/></svg>
      <h2>MANUTENÇÃO</h2>
      <p>Baixo custo de manutenção e fácil instalação.</p>
    </div>

    <div class="feature" style="left:334px;top:454px;width:140px;">
      <svg width="36" height="36" viewBox="0 0 36 36"><path d="M18 3 31 8v9c0 8-6 13-13 16C11 30 5 25 5 17V8z" fill="none" stroke="var(--navy)" stroke-width="3"/><text x="18" y="24" text-anchor="middle" font-size="14" font-weight="700" fill="var(--navy)" font-family="Roboto,sans-serif">$</text></svg>
      <h2>PROTEÇÃO</h2>
      <p>Sua conta de luz imune à inflação energética.</p>
    </div>

    <div class="feature" style="left:475px;top:454px;width:130px;">
      <svg width="36" height="36" viewBox="0 0 36 36"><path d="M10 16h5l4-11c3 0 4 2 3 6l-1 5h7c2 0 3 2 2 4l-3 10c-1 2-2 3-4 3H10z" fill="var(--navy)"/><rect x="4" y="16" width="5" height="17" fill="var(--navy)"/></svg>
      <h2>INSTALAÇÃO</h2>
      <p>A instalação é simples, fácil e rápida.</p>
    </div>

    <div class="feature" style="left:637px;top:454px;width:190px;">
      <svg width="40" height="36" viewBox="0 0 40 36"><circle cx="20" cy="11" r="6" fill="var(--navy)"/><circle cx="8" cy="14" r="4.5" fill="var(--navy)"/><circle cx="32" cy="14" r="4.5" fill="var(--navy)"/><path d="M10 32c0-8 4-12 10-12s10 4 10 12z" fill="var(--navy)"/><path d="M0 32c0-6 3-9 8-9 2 0 3 1 4 2-2 2-3 4-3 7zM40 32c0-6-3-9-8-9-2 0-3 1-4 2 2 2 3 4 3 7z" fill="var(--navy)"/></svg>
      <h2>EQUIPE</h2>
      <p>Profissionais altamente capacitados com vasta experiência em sistemas de geração e distribuição de energia.</p>
    </div>

    <div class="photo-grid" role="img" aria-label="Fotos aéreas de instalações de painéis solares em telhados">
      <div></div><div></div><div></div><div></div><div></div><div></div>
    </div>

    <div class="footer-rule"></div>
    <div class="footer-band"></div>
  </section>
</body>
</html>
```